Brightpath Strategic Advisers F.Z.E
Professional
Khalid Yousef Nasser
Founder & CEO
Corvana Trade Park
info@bsa-qx.com
www.bsa-qx.com
Training & Consultancy on:
QBXR Assessment & Training
Leadership Development & Coaching
Change Management
Strategy Management
Performance Management
Quality & Process Management
TQM
HR Development
HR Procedures & Regulation
Logo & Full Stationeries & P.P Presentation first page and continues sheet & Proposal document cover & continues sheet

```html
<!DOCTYPE html>
<html lang="en">
<head>
<meta charset="utf-8">
<title>Brightpath Strategic Advisers F.Z.E – Business Card</title>
<link href="https://fonts.googleapis.com/css2?family=Open+Sans:wght@400;600;700&display=swap" rel="stylesheet">
<style>
  :root {
    --page: #ecebe8;
    --card-top: #2a2a2a;
    --card-bottom: #050505;
    --white: #f4f4f4;
    --grey: #9a9a9a;
    --orange: #f39a1e;
    --orange-deep: #ef6a1a;
    --red: #e0281e;
    --divider: #5a5a5a;
  }
  * { margin: 0; padding: 0; box-sizing: border-box; }
  html, body {
    width: 1200px; height: 780px; overflow: hidden;
    background: var(--page);
    font-family: "Open Sans", Arial, sans-serif;
  }
  .card {
    position: absolute; left: 60px; top: 70px;
    width: 1080px; height: 640px;
    border-radius: 40px; overflow: hidden;
    background: radial-gradient(ellipse at 45% 25%, var(--card-top) 0%, #111 55%, var(--card-bottom) 100%);
    box-shadow: 0 18px 40px rgba(0,0,0,.25);
  }
  .brand {
    position: absolute; left: 0; right: 0; top: 118px;
    text-align: center;
  }
  .brand-dot {
    display: block; width: 64px; height: 64px; margin: 0 auto 26px;
    border-radius: 50%; background: var(--orange-deep);
  }
  .brand-name {
    font-weight: 600; font-size: 46px; letter-spacing: 1px;
    color: var(--white); text-transform: uppercase; line-height: 1.1;
  }
  .brand-sub {
    font-weight: 600; font-size: 30px; color: var(--white); margin-top: 4px;
  }
  .person {
    position: absolute; right: 580px; top: 382px; text-align: right;
  }
  .person-name { font-weight: 700; font-size: 30px; color: var(--orange); }
  .person-role { font-weight: 400; font-size: 24px; color: var(--grey); margin-top: 6px; }
  .divider {
    position: absolute; left: 524px; top: 340px; width: 2px; height: 176px;
    background: var(--divider);
  }
  .contact {
    position: absolute; left: 548px; top: 336px; list-style: none;
    color: var(--white); font-size: 23px;
  }
  .contact li { display: flex; align-items: center; height: 38px; }
  .contact .location { padding-left: 46px; color: var(--grey); }
  .contact svg { width: 28px; height: 28px; margin-right: 18px; flex: none; }
  .band {
    position: absolute; left: 0; right: 0; bottom: 0; height: 56px;
    background: linear-gradient(180deg, var(--orange) 0%, var(--orange-deep) 60%, var(--red) 100%);
  }
  .band::before {
    content: ""; position: absolute; left: 0; right: 0; top: -4px; height: 4px;
    background: linear-gradient(90deg, #444, #888, #444);
  }
</style>
</head>
<body>
  <div class="card">
    <div class="brand">
      <span class="brand-dot"></span>
      <div class="brand-name">Brightpath Strategic</div>
      <div class="brand-sub">Advisers F.Z.E</div>
    </div>

    <div class="person">
      <div class="person-name">Khalid Yousef Nasser</div>
      <div class="person-role">Founder &amp; CEO</div>
    </div>

    <div class="divider"></div>

    <ul class="contact">
      <li class="location">Corvana Trade Park</li>
      <li>
        <svg viewBox="0 0 24 24" aria-hidden="true"><path fill="#f39a1e" d="M6.6 10.8a15 15 0 0 0 6.6 6.6l2.2-2.2a1 1 0 0 1 1-.25 11.4 11.4 0 0 0 3.6.57 1 1 0 0 1 1 1V20a1 1 0 0 1-1 1A17 17 0 0 1 3 4a1 1 0 0 1 1-1h3.5a1 1 0 0 1 1 1c0 1.25.2 2.45.57 3.57a1 1 0 0 1-.25 1z"/></svg>
        00971505550142
      </li>
      <li>
        <svg viewBox="0 0 24 24" aria-hidden="true"><circle cx="12" cy="12" r="9" fill="none" stroke="#f39a1e" stroke-width="2"/><path d="M3 12h18M12 3c3 3 3 15 0 18M12 3c-3 3-3 15 0 18" fill="none" stroke="#f39a1e" stroke-width="1.6"/></svg>
        info@bsa-qx.com
      </li>
      <li>
        <svg viewBox="0 0 24 24" aria-hidden="true"><rect x="2" y="5" width="20" height="14" rx="2" fill="#f39a1e"/><path d="M3 6l9 7 9-7" fill="none" stroke="#111" stroke-width="1.8"/></svg>
        www.bsa-qx.com
      </li>
    </ul>

    <div class="band"></div>
  </div>
</body>
</html>
```